KVT Business Cards

We require business cards for our business. We would like a matte black back to the card, with our logo centred in the middle. The front side of the card is open to design.

Target Market(s)

Clients looking for legal services (professional)

Industry/Entity Type

Legal

Contact Information for Business Card

Boris Telemark
Partner
Mobile: 0438 715 642
Email: boris@kvtlaw.co
Website: www.kvtlaw.co
Level 3, 118 Wexbury Street
Sydney NSW 2000

Font styles to use
Other font styles liked:
• Avenir

Colors
f04a50
ffffff
1b1b1b

Requirements
Must have
• Black back with logo included in the centre of the card.
• Our font is Avenir.

```html
<!DOCTYPE html>
<html lang="en">
<head>
<meta charset="utf-8">
<title>KVT Business Cards</title>
<link rel="stylesheet" href="https://fonts.googleapis.com/css2?family=Mulish:wght@400;600;700&display=swap">
<style>
  :root {
    --brand-red: #f04a50;
    --brand-white: #ffffff;
    --brand-black: #1b1b1b;
    --back-dark: #0e0e0e;
    --ink: #2a2a2a;
    --ink-soft: #555555;
    --paper: #f4f4f4;
    --stage: #d9d9d9;
  }
  * { box-sizing: border-box; margin: 0; padding: 0; }
  html, body { width: 1200px; height: 675px; overflow: hidden; }
  body {
    background: var(--stage);
    font-family: "Mulish", "Avenir", sans-serif;
    display: flex;
    align-items: center;
    justify-content: center;
    gap: 60px;
  }
  .card {
    width: 500px;
    height: 286px;
    border-radius: 4px;
    position: relative;
    overflow: hidden;
    box-shadow: 0 10px 24px rgba(0,0,0,0.18);
  }

  /* Front */
  .card--front {
    background: linear-gradient(135deg, var(--brand-white) 0%, var(--paper) 100%);
    color: var(--ink);
    padding: 34px 36px;
  }
  .holder {
    font-size: 15px;
    letter-spacing: 0.02em;
  }
  .holder__name { font-weight: 700; text-transform: uppercase; }
  .holder__divider { margin: 0 4px; font-weight: 400; }
  .holder__role { font-size: 13px; color: var(--ink-soft); }
  .contacts {
    list-style: none;
    margin-top: 50px;
    font-size: 14px;
    line-height: 1.4;
  }
  .contacts li { display: flex; align-items: center; gap: 10px; }
  .contacts svg { width: 11px; height: 11px; fill: var(--brand-red); flex: none; }
  .contacts .web { font-weight: 700; }
  .rule {
    width: 230px;
    height: 1px;
    background: var(--brand-red);
    margin: 8px 0 8px;
  }
  .address {
    font-style: normal;
    font-size: 14px;
    line-height: 1.3;
  }
  .front-mark {
    position: absolute;
    right: 34px;
    bottom: 30px;
    display: flex;
    align-items: center;
    gap: 8px;
    font-weight: 700;
    font-size: 20px;
    color: var(--brand-black);
    letter-spacing: 0.08em;
  }
  .front-mark__square { width: 14px; height: 14px; background: var(--brand-red); }

  /* Back */
  .card--back {
    background: linear-gradient(150deg, var(--brand-black) 0%, var(--brand-black) 50%, var(--back-dark) 50%, var(--back-dark) 100%);
    display: flex;
    align-items: center;
    justify-content: center;
  }
  .back-mark { display: flex; align-items: center; gap: 14px; }
  .back-mark__square { width: 22px; height: 22px; background: var(--brand-red); }
  .back-mark__name {
    color: var(--brand-white);
    font-weight: 600;
    font-size: 17px;
    line-height: 1.15;
    letter-spacing: 0.06em;
    text-transform: uppercase;
  }
</style>
</head>
<body>
  <section class="card card--front" aria-label="Business card front">
    <p class="holder">
      <span class="holder__name">Boris Telemark</span><span class="holder__divider">|</span><span class="holder__role">Partner</span>
    </p>
    <ul class="contacts">
      <li>
        <svg viewBox="0 0 24 24" aria-hidden="true"><path d="M6.6 10.8a15.1 15.1 0 0 0 6.6 6.6l2.2-2.2a1 1 0 0 1 1-.25 11.4 11.4 0 0 0 3.6.57 1 1 0 0 1 1 1V20a1 1 0 0 1-1 1A17 17 0 0 1 3 4a1 1 0 0 1 1-1h3.5a1 1 0 0 1 1 1c0 1.25.2 2.45.57 3.6a1 1 0 0 1-.25 1z"/></svg>
        <span>0438 715 642</span>
      </li>
      <li>
        <svg viewBox="0 0 24 24" aria-hidden="true"><path d="M2 5h20v14H2zm2 2v.5l8 5 8-5V7zm0 2.8V17h16V9.8l-8 5z"/></svg>
        <span>boris@kvtlaw.co</span>
      </li>
      <li>
        <svg viewBox="0 0 24 24" aria-hidden="true"><path d="M12 2a10 10 0 1 0 0 20 10 10 0 0 0 0-20zm0 2c.9 1.2 1.6 2.6 2 4h-4c.4-1.4 1.1-2.8 2-4zM4.3 14a8 8 0 0 1 0-4h3.4a16 16 0 0 0 0 4zm.8 2h3a14 14 0 0 0 1.4 3.6A8 8 0 0 1 5.1 16zM8.1 8h-3a8 8 0 0 1 4.4-3.6A14 14 0 0 0 8.1 8zM12 20c-.9-1.2-1.6-2.6-2-4h4c-.4 1.4-1.1 2.8-2 4zm2.3-6H9.7a14 14 0 0 1 0-4h4.6a14 14 0 0 1 0 4zm.2 5.6a14 14 0 0 0 1.4-3.6h3a8 8 0 0 1-4.4 3.6zm1.8-5.6a16 16 0 0 0 0-4h3.4a8 8 0 0 1 0 4zm-.4-6a14 14 0 0 0-1.4-3.6A8 8 0 0 1 18.9 8z"/></svg>
        <span class="web">www.kvtlaw.co</span>
      </li>
    </ul>
    <div class="rule"></div>
    <address class="address">Level 3, 118 Wexbury Street<br>Sydney NSW 2000</address>
    <div class="front-mark">
      <span class="front-mark__square"></span>
      <span>KVT</span>
    </div>
  </section>

  <section class="card card--back" aria-label="Business card back">
    <div class="back-mark">
      <span class="back-mark__square"></span>
      <span class="back-mark__name">Kovar Vell<br>Telemark<br>Legal</span>
    </div>
  </section>
</body>
</html>
```